Squarespace website build: Quirk literary annual (initial design work supplied)

Our brand guidelines provide the look and feel for the website - we just need someone to create it based on our mock ups!
PLEASE NOTE:
- Please base our website off the website pages within the brief (ie homepage is GREEN)
- please ensure each page will be standalone (not a scrolling home page)
- please only use filtered duotone style photography as a hold, if you think the page needs a photo.
-please not the websites i have provided as an influence - especially TIDE YEARLY. We want very little photography.

Quirk is a literary and arts journal that provides a platform for both emerging and established writers and artists from New Zealand and beyond. We are passionate about sharing insights into the intimate and unique worlds of creatives with short stories, poetry, and art – showcasing raw and unfiltered glimpses into their world.

We have our brand guidelines and logo finalised, with a 'look and feel' design for the website within our attached brand guidelines document. We just need someone to design this simple website on Squarespace for us. It will have five pages and will need a newsletter sign up link:
Home page
About us page
Submissions page
Purchase page
Contact page

DRAFT WEB COPY

ABOUT
QUIRK is an independent literary annual journal established in 2022 by Hazel Wintergate and Mereana Clift that publishes unrepentant unfiltered accounts of life, eclectic takes on the mundane ordinary, and deep dives into modern love & sexuality.
Founder, Editor: Hazel Arohanui Wintergate
Founder, Production Director: Mereana Clift
Art Direction: Lorna Pike
Editorial Assistant: Kirsten Holloway-Dunn

I suggest duotone fashion-esque photography which is very Vesna Kordell/ Palm Springs vibe but not obviously identifiable.
· I love the style of Rufus Tennick for our shoot in particular. Group lazing around a pool, leisurely, glam, but effortless and ironically looking very natural – as though – yes, these are our lives.
SUBMISSION PAGE
Quirk welcomes submissions all year round.
We are drawn to dark humour, satirical takes on the social scene, and starkly honest accounts of ordinary life. Diversity is celebrated, adversity is welcomed and, above all, personal expression is championed. We are particularly seeking content that takes risks, screams of honesty and celebrates life’s most extraordinary moments.
Selected works will be published in our annual publication.

Submission guidelines
We accept flash fiction, short stories and poetry. Individual entries not to mustn’t exceed 2000 words.
Submitted work must be unpublished and in English. We welcome simultaneous submissions, but must be notified immediately if your manuscript is accepted for publication elsewhere or appears in any print or online source. We will endeavour to respond to all submissions within four weeks.
Please send submissions as a word document along with a brief bio of 50 words to pages@quirkjournal.test
PO Box[EB2]
​Note on Copyright: Copyright remains with the author.

Annual short story competition
Volume Alpha is interested in all that is spiritual, coincidental, or mysterious. Stories selected for this issue reflect life’s uncanny moments, those that defy explanation, and experiences that promote personal and spiritual growth. Entires must be no longer than 2000 words.

First prize: 1000
Second prize: 500
Third prize: 200[EB3]

SUPPORT US
Since our launch in 2022, we have relied upon the generous support of our creative business community in Wellington City, New Zealand. If you read us, or love our ethos, please consider a donation.
Link to chipinhere page
Updates

Hello designers
I would ideally love to have someone turn this around within a few weeks, because the design work has mostly been provided.
Thanks
Hazel

Hi everyone Please ensure you read our brand guidelines and follow the brief. Please note we do not yet have a product, as this is a new venture, so there is no point including images of a magazine that doesn't yet exist. Some further comment to ensure we get there: - We want all pages to be separate pages (not a scrolling home page) with a different colour based on the guidelines - The home page must look just as it does in the brand guidelines - There is no archive page (please read brief) as we have no archive yet. The pages are: Home, About, Contact, Competitions and submissions Thank you

Target Market(s)

writers and creatives

Industry/Entity Type

Writing/ creative/ publishing

Coding

Coded - Design and coding required

Number of Pages Required

4 page

Font styles to use
Other font styles liked:
• COTTA and Univers - as per brand guidelines

Requirements
Must have
• Squarespace designer needed to design our mocked up webpages.
Nice to have
• As close to the brand guideline mock ups as possible (see page 11,12,13)
Should not have
• anything outside of the brand guidelines

```html
<!DOCTYPE html>
<html lang="en">
<head>
<meta charset="utf-8">
<title>Quirk — Home</title>
<link rel="stylesheet" href="https://fonts.googleapis.com/css2?family=Fraunces:opsz,wght@9..144,400&family=Roboto+Condensed:wght@400&family=Figtree:wght@400&display=swap">
<style>
  :root {
    --olive: #667a37;
    --olive-pattern: #6a7e3b;
    --olive-deep: #5f7231;
    --gold: #b9a033;
    --cream: #ffffff;
  }
  * { margin: 0; padding: 0; box-sizing: border-box; }
  html, body {
    width: 1200px;
    height: 478px;
    overflow: hidden;
    background: var(--olive);
  }
  .page {
    position: relative;
    width: 1200px;
    height: 478px;
    color: var(--cream);
  }
  .hero-backdrop {
    position: absolute;
    inset: 0 0 54px 0;
    background: radial-gradient(ellipse at center, var(--olive-pattern), var(--olive));
  }
  .site-nav a {
    position: absolute;
    top: 57px;
    font-family: "Roboto Condensed", sans-serif;
    font-size: 12px;
    letter-spacing: 0.2px;
    color: var(--cream);
    text-decoration: none;
    line-height: 16px;
  }
  .nav-rule {
    position: absolute;
    top: 65px;
    height: 1px;
    background: var(--cream);
  }
  .brand {
    position: absolute;
    left: 0;
    width: 1200px;
    top: 44px;
    height: 50px;
    display: flex;
    align-items: center;
    justify-content: center;
    gap: 12px;
    text-decoration: none;
  }
  .brand-mark {
    width: 14px;
    height: 14px;
    background: var(--gold);
  }
  .brand-name {
    font-family: "Fraunces", serif;
    font-weight: 400;
    font-size: 40px;
    line-height: 50px;
    color: var(--gold);
  }
  .hero-title {
    position: absolute;
    left: 0;
    width: 1200px;
    top: 186px;
    text-align: center;
    font-family: "Fraunces", serif;
    font-weight: 400;
    font-size: 34px;
    line-height: 48px;
    letter-spacing: -0.2px;
  }
  .hero-button {
    position: absolute;
    left: 538px;
    top: 302px;
    width: 124px;
    height: 46px;
    border: 2px solid var(--gold);
    display: flex;
    align-items: center;
    justify-content: center;
    font-family: "Roboto Condensed", sans-serif;
    font-size: 14px;
    letter-spacing: 0.8px;
    color: var(--cream);
    text-decoration: none;
  }
  .site-footer {
    position: absolute;
    left: 0;
    bottom: 0;
    width: 1200px;
    height: 54px;
    background: var(--olive-deep);
  }
  .copyright {
    position: absolute;
    left: 162px;
    top: 17px;
    font-family: "Figtree", sans-serif;
    font-size: 14px;
    line-height: 18px;
  }
  .social-link {
    position: absolute;
    top: 12px;
    width: 30px;
    height: 30px;
    border: 1px solid var(--gold);
    display: flex;
    align-items: center;
    justify-content: center;
  }
  .social-dot {
    width: 10px;
    height: 10px;
    border-radius: 50%;
    background: var(--cream);
  }
</style>
</head>
<body>
  <div class="page">
    <div class="hero-backdrop" role="img" aria-label="Olive background with a faint repeating star-and-circle pattern"></div>

    <nav class="site-nav">
      <a href="#" style="left:248px">HOME</a>
      <span class="nav-rule" style="left:287px;width:23px"></span>
      <a href="#" style="left:322px">ABOUT</a>
      <span class="nav-rule" style="left:366px;width:23px"></span>
      <a href="#" style="left:400px">CONTACT</a>

      <a href="#" style="left:730px">COMPETITIONS</a>
      <span class="nav-rule" style="left:815px;width:23px"></span>
      <a href="#" style="left:849px">SUBMISSIONS</a>
    </nav>

    <a class="brand" href="#">
      <span class="brand-mark"></span>
      <span class="brand-name">quirk</span>
    </a>

    <h1 class="hero-title">Quirk Is A Plucky Little Publication Out<br>of Wellington, New Zealand</h1>

    <a class="hero-button" href="#">KNOW MORE</a>

    <footer class="site-footer">
      <p class="copyright">Copyright © 2022 quirk. All Rights Reserved.</p>
      <a class="social-link" href="#" aria-label="Social profile 1" style="left:895px"><span class="social-dot"></span></a>
      <a class="social-link" href="#" aria-label="Social profile 2" style="left:933px"><span class="social-dot"></span></a>
      <a class="social-link" href="#" aria-label="Social profile 3" style="left:971px"><span class="social-dot"></span></a>
      <a class="social-link" href="#" aria-label="Social profile 4" style="left:1010px"><span class="social-dot"></span></a>
    </footer>
  </div>
</body>
</html>
```